Computer company startup need wordpress template

I am looking for a new design that is fresh, bold and stands out from the crowd for an IT company called Torvane Computers. We specialise in consumer and small business IT.

It will have to be mobile friendly, viewable on all devices. I need a template that i can work with and that will give our site a professional look and feel but not look like every other site out there.

To see what text will be on final site, see www.torvanecomputers-demo.com.au, i will change wording, but it is pretty close to what it's meant to be.

I have supplied logo and the main colours on car, business cards etc is black, red (and shades thereof) and white.

I am visualiing some home page with "Welcome to Torvane Computers, how may we help you today?" then 4 cool looking buttons below which says:

1. Residential computer / network issues
2. Business computer / network issues
3. Home Networking
4. New home networking

These buttons will then take you to the correct page which i will flesh out from the template. All pages need have sections for my support links etc.

Website built from template will have 5-6 pages max.

If anyone need any additional direction, please send me a message and i will answer.

Target Market(s)

Consumer and small business (1-20 employees) customers

Industry/Entity Type

It Company

Requirements
Must have
• professional look and feel

```html
<!DOCTYPE html>
<html lang="en">
<head>
<meta charset="utf-8">
<title>Torvane Computers</title>
<link href="https://fonts.googleapis.com/css2?family=Roboto+Condensed:wght@300;400;700&family=Open+Sans:wght@400;600&display=swap" rel="stylesheet">
<style>
  :root {
    --red: #e5202a;
    --red-dark: #b8141c;
    --ink: #222222;
    --grey: #6b6b6b;
    --navy: #1a2230;
    --navy-deep: #111822;
    --black: #0c0c0c;
    --white: #ffffff;
    --light: #f2f2f2;
  }
  * { box-sizing: border-box; margin: 0; padding: 0; }
  html, body { width: 706px; height: 1200px; overflow: hidden; background: var(--white); }
  body { font-family: "Open Sans", Arial, sans-serif; color: var(--ink); position: relative; }
  .cond { font-family: "Roboto Condensed", Arial, sans-serif; }

  /* hero */
  .hero { position: relative; height: 348px; }
  .hero-photo { position: absolute; inset: 0;
    background: radial-gradient(ellipse at 45% 55%, #cfd3d8 0%, #9ea4ab 40%, #e9ebee 75%, #f7f7f7 100%); }
  .brand { position: absolute; left: 18px; top: 18px; background: var(--white); padding: 8px 14px;
    display: flex; align-items: center; gap: 8px; }
  .brand-dot { width: 14px; height: 14px; border-radius: 50%; background: var(--red); }
  .brand-name { font-family: "Roboto Condensed", Arial, sans-serif; font-weight: 700; font-size: 20px; color: var(--red); }
  .main-nav { position: absolute; right: 20px; top: 34px; display: flex; gap: 30px;
    font-family: "Roboto Condensed", Arial, sans-serif; font-size: 14px; text-transform: uppercase; }
  .main-nav a { color: var(--ink); text-decoration: none; }
  .main-nav a.active { color: var(--red); }

  /* call band */
  .call-band { height: 76px; background: var(--red); color: var(--white); display: flex; align-items: center;
    justify-content: center; gap: 36px; font-family: "Roboto Condensed", Arial, sans-serif; font-size: 24px; }
  .call-band .call { display: flex; align-items: center; gap: 12px; }
  .phone-ring { width: 38px; height: 38px; border-radius: 50%; border: 2px solid var(--white);
    display: flex; align-items: center; justify-content: center; }

  /* welcome */
  .welcome { height: 183px; text-align: center; padding: 28px 90px 0; }
  .welcome h1 { font-family: "Roboto Condensed", Arial, sans-serif; font-weight: 300; font-size: 34px;
    color: var(--ink); letter-spacing: 0.5px; margin-bottom: 22px; }
  .welcome p { font-size: 9.5px; line-height: 1.55; color: var(--grey); margin-bottom: 12px; }

  /* services */
  .services { height: 283px; background: linear-gradient(180deg, var(--navy) 0%, var(--navy-deep) 100%);
    display: flex; justify-content: center; gap: 5px; padding-top: 40px; }
  .service { width: 148px; text-align: center; }
  .service-photo { height: 92px; background: linear-gradient(135deg, #cfe2ef, #8fb0c8); margin-bottom: 10px; }
  .service:nth-child(4) .service-photo { background: linear-gradient(135deg, #2d5fa8, #0e1f44); }
  .service:nth-child(3) .service-photo { background: linear-gradient(135deg, #d9dde2, #7d8590); }
  .service h2 { font-family: "Roboto Condensed", Arial, sans-serif; font-weight: 400; font-size: 13px;
    color: var(--red); line-height: 1.2; height: 32px; }
  .service p { font-size: 8.5px; color: #d4d7dc; line-height: 1.45; margin: 6px 12px 12px; }
  .read-more { display: inline-block; background: var(--red); color: var(--white); font-family: "Roboto Condensed", Arial, sans-serif;
    font-size: 11px; padding: 5px 12px; text-decoration: none; }

  /* partners */
  .partners { height: 117px; display: flex; align-items: center; justify-content: space-between; padding: 0 22px; }
  .partner-list { display: flex; gap: 26px; align-items: center; }
  .partner { width: 62px; height: 26px; background: #d5d7da; border-radius: 3px; }

  /* remote */
  .remote { height: 76px; position: relative; }
  .remote-banner { position: absolute; left: 47px; top: 10px; width: 440px; height: 56px;
    color: var(--white); font-size: 11px; line-height: 1.4; padding: 12px 40px 0 50px; }
  .remote-banner svg { position: absolute; inset: 0; z-index: -1; }
  .remote-badge { position: absolute; left: 466px; top: 4px; width: 194px; height: 68px;
    display: flex; align-items: center; justify-content: center; gap: 8px; }
  .remote-badge svg { position: absolute; inset: 0; }
  .remote-name { position: relative; color: var(--white); font-family: "Roboto Condensed", Arial, sans-serif; font-size: 20px; font-weight: 400; }

  /* footer */
  .footer-nav { height: 40px; display: flex; justify-content: center; align-items: center; gap: 28px;
    font-family: "Roboto Condensed", Arial, sans-serif; font-size: 13px; text-transform: uppercase; }
  .footer-nav a { color: var(--ink); text-decoration: none; }
  .footer-nav a.active { color: var(--red); }
  .site-footer { height: 77px; background: var(--black); display: flex; justify-content: space-between;
    align-items: center; padding: 0 44px; color: var(--white); }
  .footer-links { display: flex; gap: 16px; font-size: 9px; margin-bottom: 8px; }
  .copyright { font-size: 7.5px; color: #9a9a9a; }
  .copyright span { color: var(--red); }
  .social { display: flex; gap: 18px; }
  .social span { width: 32px; height: 32px; border-radius: 50%; border: 1.5px solid var(--red); display: block; }
</style>
</head>
<body>
  <header class="hero">
    <div class="hero-photo" role="img" aria-label="Photo of hands typing on a laptop keyboard"></div>
    <div class="brand"><span class="brand-dot"></span><span class="brand-name">Torvane Computers</span></div>
    <nav class="main-nav">
      <a class="active" href="#">Home</a><a href="#">About</a><a href="#">Services</a><a href="#">FAQ</a><a href="#">Contact</a>
    </nav>
  </header>

  <section class="call-band">
    <span>How may we help you today?</span>
    <span class="call">CALL US ON :
      <span class="phone-ring">
        <svg width="18" height="18" viewBox="0 0 24 24"><path fill="#fff" d="M6.6 10.8a15.1 15.1 0 0 0 6.6 6.6l2.2-2.2c.3-.3.7-.4 1-.2 1.1.4 2.3.6 3.6.6.6 0 1 .4 1 1V20c0 .6-.4 1-1 1A17 17 0 0 1 3 4c0-.6.4-1 1-1h3.5c.6 0 1 .4 1 1 0 1.3.2 2.5.6 3.6.1.3 0 .7-.2 1z"/></svg>
      </span>
      0400 555 182</span>
  </section>

  <section class="welcome">
    <h1>WELCOME TO TORVANE COMPUTERS</h1>
    <p>Torvane Computers deliver expert onsite computer services to small business and home owners in Southern Tasmania. We specialise in IT security, custom built computers and general computer repair.</p>
    <p>Our expert staff will also help you with training and pre-purchase advice to what suits your business or family best, and what will also future proof you in the areas where your system will be utilised the most.</p>
  </section>

  <section class="services">
    <article class="service">
      <div class="service-photo" role="img" aria-label="Photo of a woman using a laptop at home"></div>
      <h2>Residential computer / network issues</h2>
      <p>Lorem ipsum is simply dummy text of the printing and typesetting industry.</p>
      <a class="read-more" href="#">READ MORE</a>
    </article>
    <article class="service">
      <div class="service-photo" role="img" aria-label="Photo of a business woman working at a laptop"></div>
      <h2>Business computer / network issues</h2>
      <p>Lorem ipsum is simply dummy text of the printing and typesetting industry.</p>
      <a class="read-more" href="#">READ MORE</a>
    </article>
    <article class="service">
      <div class="service-photo" role="img" aria-label="Photo of hands on a laptop keyboard"></div>
      <h2>Home networking</h2>
      <p>Lorem ipsum is simply dummy text of the printing and typesetting industry.</p>
      <a class="read-more" href="#">READ MORE</a>
    </article>
    <article class="service">
      <div class="service-photo" role="img" aria-label="Photo of network cables plugged into a switch"></div>
      <h2>New home networking</h2>
      <p>Lorem ipsum is simply dummy text of the printing and typesetting industry.</p>
      <a class="read-more" href="#">READ MORE</a>
    </article>
  </section>

  <section class="partners">
    <svg width="12" height="22" viewBox="0 0 12 22"><path d="M10 2 2 11l8 9" fill="none" stroke="#e5202a" stroke-width="2.5"/></svg>
    <div class="partner-list">
      <span class="partner"></span><span class="partner"></span><span class="partner"></span><span class="partner"></span>
      <span class="partner"></span><span class="partner"></span><span class="partner"></span>
    </div>
    <svg width="12" height="22" viewBox="0 0 12 22"><path d="M2 2l8 9-8 9" fill="none" stroke="#222" stroke-width="2.5"/></svg>
  </section>

  <section class="remote">
    <div class="remote-banner">
      <svg width="440" height="56" viewBox="0 0 440 56"><polygon points="24,0 440,0 440,56 24,56 0,28" fill="#e5202a"/></svg>
      If requested by our staff to do so, please click on this link to start our Remote Assistance Software.
    </div>
    <div class="remote-badge">
      <svg width="194" height="68" viewBox="0 0 194 68"><polygon points="24,0 170,0 194,34 170,68 24,68 0,34" fill="#0c0c0c"/></svg>
      <span class="remote-name">DeskReach</span>
    </div>
  </section>

  <nav class="footer-nav">
    <a class="active" href="#">Home</a><a href="#">About</a><a href="#">Services</a><a href="#">FAQ</a><a href="#">Contact</a>
  </nav>

  <footer class="site-footer">
    <div>
      <div class="footer-links"><span>Home</span><span>About</span><span>Services</span><span>Faq</span><span>News</span><span>Contact</span></div>
      <div class="copyright">© <span>TORVANE COMPUTERS</span> - 2015, All Rights Reserved.</div>
    </div>
    <div class="social"><span></span><span></span><span></span></div>
  </footer>
</body>
</html>
```